Business Card Design

The Wren Hollow Inn is the most centrally located motel in Grafton.
We are the only family owned motel in Grafton.
Our colour scheme is blue, whiteand black.

I have uploaded a photo of our new rooms and the logo for you to use Thanks. Looking good

Industry/Entity Type

Motel

Contact Information for Business Card

The Wren Hollow Inn
Marcus & Helena Dobrev
Owner/Operators
14-16 Pellham Street, Grafton NSW 2460
Ph: 02 6690 3457
Email: thewrenhollowinn@mailbox.example
reception@wrenhollowinn.example
www.wrenhollowinn.example

Colors
0392cd
0455a3

```html
<!DOCTYPE html>
<html lang="en">
<head>
<meta charset="utf-8">
<title>The Wren Hollow Inn – Business Card</title>
<link rel="stylesheet" href="https://fonts.googleapis.com/css2?family=Lato:wght@400;700&display=swap">
<style>
  :root {
    --page-bg: #e6e6e6;
    --ink: #1f1f1f;
    --blue-deep: #0455a3;
    --blue-bright: #0392cd;
    --band-1: #2f7db6;
    --band-2: #3a88c0;
    --band-3: #4593c8;
    --band-4: #4f9dcf;
    --band-5: #55a5d4;
    --band-6: #5eabd7;
    --band-7: #6ab2da;
    --band-8: #78badd;
    --veil: rgba(255, 255, 255, 0.55);
    --footer-band: rgba(90, 96, 104, 0.35);
  }

  * { margin: 0; padding: 0; box-sizing: border-box; }

  html, body {
    width: 1200px;
    height: 772px;
    overflow: hidden;
    background: var(--page-bg);
  }

  .card {
    position: absolute;
    left: 50px;
    top: 71px;
    width: 1100px;
    height: 630px;
    overflow: hidden;
    font-family: "Lato", "Helvetica Neue", Arial, sans-serif;
    color: var(--ink);
    text-align: center;
  }

  .room-photo {
    position: absolute;
    inset: 0;
    background:
      linear-gradient(90deg, rgba(176, 140, 96, 0.45) 0%, rgba(176, 140, 96, 0.25) 28%, rgba(255, 255, 255, 0) 45%),
      linear-gradient(180deg, #e9e7e2 0%, #dcd8d0 45%, #c9ccd0 75%, #bfc4ca 100%);
  }

  .room-photo::after {
    content: "";
    position: absolute;
    inset: 0;
    background: var(--veil);
  }

  .top-band {
    position: absolute;
    left: 0;
    top: 0;
    width: 100%;
    height: 34px;
    display: flex;
  }

  .top-band span { flex: 1; }
  .top-band span:nth-child(1) { background: var(--band-1); }
  .top-band span:nth-child(2) { background: var(--band-2); }
  .top-band span:nth-child(3) { background: var(--band-3); }
  .top-band span:nth-child(4) { background: var(--band-4); }
  .top-band span:nth-child(5) { background: var(--band-5); }
  .top-band span:nth-child(6) { background: var(--band-6); }
  .top-band span:nth-child(7) { background: var(--band-7); }
  .top-band span:nth-child(8) { background: var(--band-8); }

  .footer-band {
    position: absolute;
    left: 0;
    bottom: 0;
    width: 100%;
    height: 16px;
    background: var(--footer-band);
  }

  .line {
    position: absolute;
    left: 0;
    width: 100%;
    white-space: nowrap;
  }

  .operators-names {
    top: 81px;
    height: 40px;
    line-height: 40px;
    font-size: 30px;
    letter-spacing: 0.5px;
  }

  .operators-role {
    top: 132px;
    height: 28px;
    line-height: 28px;
    font-size: 21px;
    letter-spacing: 0.5px;
  }

  .title-band {
    position: absolute;
    left: 0;
    top: 231px;
    width: 100%;
    height: 88px;
    background: rgba(255, 255, 255, 0.6);
  }

  .inn-name {
    top: 241px;
    height: 60px;
    line-height: 60px;
    font-size: 47px;
    letter-spacing: 1.5px;
    text-transform: uppercase;
    color: #151515;
  }

  .contact {
    height: 36px;
    line-height: 36px;
    font-size: 27px;
    letter-spacing: 0.3px;
  }

  .contact.phone { top: 386px; }
  .contact.email { top: 441px; }
  .contact.address { top: 498px; }
</style>
</head>
<body>
  <main class="card">
    <div class="room-photo" role="img" aria-label="Photo of the inn's renovated room with kitchenette, timber cabinets, ceiling fan and glass dining table"></div>

    <div class="top-band" aria-hidden="true">
      <span></span><span></span><span></span><span></span>
      <span></span><span></span><span></span><span></span>
    </div>

    <p class="line operators-names">Marcus &amp; Helena Dobrev</p>
    <p class="line operators-role">Operators</p>

    <div class="title-band" aria-hidden="true"></div>
    <h1 class="line inn-name">The Wren Hollow Inn</h1>

    <p class="line contact phone">02 6690 3457</p>
    <p class="line contact email">thewrenhollowinn@mailbox.example</p>
    <p class="line contact address">14-16 Pellham Street, Grafton NSW 2460</p>

    <div class="footer-band" aria-hidden="true"></div>
  </main>
</body>
</html>
```